Real Estate Agent Service Brochure

I need a trifold brochure to showcase my real estate services. I am a veteran Real Estate Broker specializing in marketing properties for sale and for top dollar. I would like to see designs that use colors from my logo (attached) and I would like to showcase some before and after photos of staging jobs I have done to homes to get them ready for the market. This brochure is specific to home sellers. You are happy to go check out my website for inspiration www.lomavertpa.com but keep the copy as I have written it. The the final design should communicate experienced professional who uses current technologies and strategies to market properties for the highest value.

Target Market(s)

Homeowners wanting to sell their homes

Industry/Entity Type

Real Estate Agent

Font styles to use
Serif

Requirements
Must have
• My, logo, personal photo, title and contact information as listed:
• Marta Venholt
• Owner Broker
• Stager Re-Designer
• 860-912-7048
• BRAVE Realty LLC
• LOMAVERTPA.com
• Marta@LOMAVERTPA.com
• The colors used should be those in my logo.
• Brochure should be able to fit in standard envelope for mailing.
Nice to have
• I think I would like my personal photo and contact information on the front panel.
Should not have
• Bright colors.

```html
<!DOCTYPE html>
<html lang="en">
<head>
<meta charset="utf-8">
<title>BRAVE Realty LLC – Seller Brochure</title>
<link href="https://fonts.googleapis.com/css2?family=Montserrat:wght@500;700&family=Lora:ital,wght@0,400;0,600;1,400&display=swap" rel="stylesheet">
<style>
:root{
  --navy:#1e2a55;
  --slate:#6b7384;
  --line:#c9ccd4;
  --paper:#ffffff;
  --ground:#e4e5e8;
  --photo-a:#b9b3a8;
  --photo-b:#7d776c;
}
*{margin:0;padding:0;box-sizing:border-box}
html,body{width:807px;height:1200px;overflow:hidden;background:var(--ground)}
body{position:relative;font-family:"Lora",serif;color:#333}
.sheet{position:absolute;left:14px;width:779px;height:568px;background:var(--paper);display:flex;box-shadow:0 2px 8px rgba(0,0,0,.15)}
.sheet--outside{top:20px}
.sheet--inside{top:612px}
.panel{position:relative;width:33.333%;height:100%;padding:22px 20px}
.panel--navy{background:var(--navy);color:#fff}
h3{font-family:"Montserrat",sans-serif;font-weight:700;font-size:11px;letter-spacing:.08em;text-transform:uppercase}
p{font-size:9.5px;line-height:1.45}
.feature{display:flex;gap:10px;margin-bottom:20px}
.feature svg{flex:none}
.feature h3{margin-bottom:6px}
.feature p{color:#dfe3ee}
.banner{background:var(--navy);color:#fff;font-family:"Montserrat",sans-serif;font-size:9px;font-weight:700;letter-spacing:.1em;text-align:center;padding:5px 0;margin-bottom:10px}
.intro{text-align:center;color:#444}
.brand{display:flex;align-items:center;gap:8px;font-family:"Lora",serif;font-weight:600;color:var(--navy);white-space:nowrap}
.brand i{display:block;flex:none;background:var(--navy);border-radius:50%}
.photo{position:absolute;background:linear-gradient(160deg,var(--photo-a),var(--photo-b))}
.web{position:absolute;left:0;right:0;text-align:center;font-family:"Montserrat",sans-serif;font-weight:700;font-size:10px;color:var(--navy);letter-spacing:.06em}
.contact{font-size:9.5px;line-height:1.7;color:#333}
.contact strong{font-family:"Montserrat",sans-serif;font-size:12px;color:var(--navy)}
.rule{height:1px;background:var(--line);margin:8px 0}
.quote{margin-bottom:11px;color:#444}
.quote b{display:block;text-align:right;font-family:"Montserrat",sans-serif;font-size:9px;color:var(--navy);margin-top:3px}
.grid{position:absolute;left:20px;right:20px;bottom:20px;height:250px;background:var(--navy);padding:8px;display:grid;grid-template-columns:1fr 1fr;gap:6px}
.grid div{position:relative;background:linear-gradient(160deg,var(--photo-a),var(--photo-b))}
.grid span{position:absolute;left:0;bottom:0;background:var(--navy);color:#fff;font-family:"Montserrat",sans-serif;font-size:8px;font-weight:700;padding:2px 6px;letter-spacing:.08em}
.navy-box{background:var(--navy);color:#fff;padding:12px}
</style>
</head>
<body>

<section class="sheet sheet--outside">
  <div class="panel panel--navy">
    <div class="feature">
      <svg width="26" height="26" viewBox="0 0 26 26"><circle cx="13" cy="13" r="12" fill="none" stroke="#fff" stroke-width="1.5"/><path d="M7 16l4-4 3 3 5-6" fill="none" stroke="#fff" stroke-width="1.5"/></svg>
      <div><h3>Adapting the New Trends</h3><p>Selling real estate has changed greatly in recent years. Today's buyers search online first, so every listing needs strong photos, sharp copy and smart digital exposure from day one to stand out.</p></div>
    </div>
    <div class="feature">
      <svg width="26" height="26" viewBox="0 0 26 26"><circle cx="13" cy="13" r="12" fill="none" stroke="#fff" stroke-width="1.5"/><path d="M8 13l3 3 7-7" fill="none" stroke="#fff" stroke-width="1.5"/></svg>
      <div><h3>Reliable Partnership</h3><p>Having the right partner is vital when you sell your home. You need someone who protects your interests, guides every step and keeps you informed through the whole process.</p></div>
    </div>
    <div class="feature">
      <svg width="26" height="26" viewBox="0 0 26 26"><circle cx="13" cy="13" r="12" fill="none" stroke="#fff" stroke-width="1.5"/><circle cx="13" cy="13" r="6" fill="none" stroke="#fff" stroke-width="1.5"/><circle cx="13" cy="13" r="1.8" fill="#fff"/></svg>
      <div><h3>Targeting the Right Buyers</h3><p>Marta uses a proven marketing plan that blends staging, online ads and local outreach so your home reaches qualified buyers who are ready and able to pay top dollar.</p></div>
    </div>
    <div class="feature">
      <svg width="26" height="26" viewBox="0 0 26 26"><circle cx="13" cy="13" r="12" fill="none" stroke="#fff" stroke-width="1.5"/><path d="M8 15q5 5 10 0" fill="none" stroke="#fff" stroke-width="1.5"/><circle cx="9.5" cy="10" r="1.3" fill="#fff"/><circle cx="16.5" cy="10" r="1.3" fill="#fff"/></svg>
      <div><h3>Happy Sellers Guaranteed</h3><p>A home is one of your largest assets. When you are ready to sell, it is vital that you are represented by an agent who puts your goals first.</p></div>
    </div>
  </div>

  <div class="panel">
    <div class="banner">PROVEN MARKET ADVANTAGE</div>
    <p class="intro">Marta has over twenty years of experience helping homeowners sell. Her staging and design background lets her present each property at its very best, attracting more buyers and stronger offers in any market.</p>
  </div>

  <div class="panel">
    <div class="brand" style="font-size:18px;justify-content:flex-end;margin-top:30px"><i style="width:12px;height:12px"></i>BRAVE Realty LLC</div>
  </div>

  <div class="photo" role="img" aria-label="Staged living room interior with windows and furniture" style="left:279px;top:150px;width:500px;height:190px"></div>

  <div style="position:absolute;left:375px;top:350px;display:flex;flex-direction:column;gap:6px">
    <svg width="14" height="14"><circle cx="7" cy="7" r="7" fill="var(--navy)"/></svg>
    <svg width="14" height="14"><circle cx="7" cy="7" r="7" fill="var(--slate)"/></svg>
    <svg width="14" height="14"><circle cx="7" cy="7" r="7" fill="var(--navy)"/></svg>
  </div>

  <div class="contact" style="position:absolute;left:540px;top:352px;width:120px">
    <strong>Marta Venholt</strong><br>Owner Broker<br>Stager Re-Designer<div class="rule"></div>
    <svg width="9" height="9" viewBox="0 0 10 10"><path d="M2 1l2 2-1 1.5q1 2 3 3L7.5 6.5l2 2-1.5 1.5Q2 9 0.5 2.5z" fill="var(--navy)"/></svg> 860-912-7048<br>
    Marta@LOMAVERTPA.com
  </div>
  <div class="photo" role="img" aria-label="Portrait of the broker" style="left:665px;top:345px;width:105px;height:170px;background:linear-gradient(180deg,#c8c9cc,#5a6070)"></div>

  <div class="web" style="left:520px;width:259px;bottom:18px">www.LOMAVERTPA.com</div>
</section>

<section class="sheet sheet--inside">
  <div class="panel">
    <div style="display:flex;gap:10px;align-items:flex-start">
      <div class="photo" role="img" aria-label="Round portrait of the broker" style="position:relative;flex:none;width:64px;height:64px;border-radius:50%;background:linear-gradient(180deg,#c8c9cc,#5a6070)"></div>
      <p>A veteran in the real estate industry, Marta brings deep market knowledge and a designer's eye to every listing. As an owner broker and home stager, she knows what buyers want and how to show it.</p>
    </div>
    <div class="brand" style="font-size:20px;justify-content:center;margin-top:50px"><i style="width:14px;height:14px"></i>BRAVE Realty LLC</div>
    <div class="navy-box" style="margin-top:56px"><p>Marta sets herself apart by staging each home before it ever hits the market. This extra care creates strong first impressions, shortens time on market and helps sellers walk away with a higher final sale price.</p></div>
  </div>

  <div class="panel" style="border-left:1px solid var(--line);border-right:1px solid var(--line)">
    <h3 style="color:var(--navy);margin-bottom:12px;line-height:1.4">This is what Marta's clients say about their experiences</h3>
    <p class="quote">"I have had several real estate dealings with Marta over the years and she has been wonderful every time. Her staging made our house look brand new and it sold in days."<b>Dana R.</b></p>
    <p class="quote">"We could not be more pleased with Marta. She was honest, organized and always available to answer our questions. Our home sold above asking price."<b>Lou &amp; Ana T.</b></p>
    <p class="quote">"From the first meeting Marta had a clear plan. Her photos and online marketing brought in many buyers and we had several offers the first weekend."<b>Nora W.</b></p>
    <p class="quote">"Marta's eye for design is amazing. She rearranged our rooms with what we had and the change was remarkable."<b>Ivy L.</b></p>
  </div>

  <div class="panel">
    <p class="quote">"Marta listened to our needs from the very start and guided us through every detail of the sale. We would gladly work with her again and recommend her to friends."<b>Sam K.</b></p>
    <div class="web" style="top:150px">www.LOMAVERTPA.com</div>
    <div class="grid">
      <div role="img" aria-label="Room before staging"><span>BEFORE</span></div>
      <div role="img" aria-label="Room after staging"><span>AFTER</span></div>
      <div role="img" aria-label="Room before staging"><span>BEFORE</span></div>
      <div role="img" aria-label="Room after staging"><span>AFTER</span></div>
      <div role="img" aria-label="Room before staging"><span>BEFORE</span></div>
      <div role="img" aria-label="Room after staging"><span>AFTER</span></div>
    </div>
  </div>
</section>

</body>
</html>
```